Business Name is TL Glamworks - Make-up Artist

I'm looking for an attractive and eye catching business card for for mobile make-up artist business. On the front of the card, I just want the name TL Glamworks in feminine type cursive writing and underneath my name Tessa Lowrie and Make-Up Artist.
On the back of the card, I would like written down one side the following;
Make-Up Tutorials
Bridal
Photography
Debutante
Formals
Family Portraits
I would also like the following details as well as the Chatterbook and Snapgram Icons;
Mobile: 0462 318 725
Email: tessalowrie@mailbox-demo.com
Website: tessalowrie.velmora-demo.com
Certificate III in Make-Up
Also, I would like a section that says Your Next Appointment and a space to put that information.
I would also like the Velmora Symbol on the bottom right hand corner (I have attached)

Target Market(s)

Mostly females

Industry/Entity Type

Makeup

Contact Information for Business Card

TL Glamworks
Tessa Lowrie - Make-Up Artist

Font styles to use
Script

Colors
b768aa
886aae
e34297

Requirements
Must have
• Mobile: 0462 318 725
• Email: tessalowrie@mailbox-demo.com
• Website: tessalowrie.velmora-demo.com
• Certificate III in Make-Up
Nice to have
• Something to do with make-up like a smudged lipstick or some eye shadow
Should not have
• Don't want it too busy

```html
<!DOCTYPE html>
<html lang="en">
<head>
<meta charset="utf-8">
<title>TL Glamworks – Business Card</title>
<link href="https://fonts.googleapis.com/css2?family=Mulish:ital,wght@0,300;0,400;0,700;1,400&display=swap" rel="stylesheet">
<style>
  :root{
    --backdrop:#1b1b1b;
    --card:#fbfbfb;
    --pink:#e0177d;
    --purple:#6e5fa8;
    --ink:#454545;
    --rule:#555;
    --partner:#16913a;
  }
  *{box-sizing:border-box;margin:0;padding:0}
  html,body{width:1200px;height:1118px;overflow:hidden}
  body{background:var(--backdrop);font-family:"Mulish",sans-serif;color:var(--ink);position:relative}
  .card{position:absolute;left:292px;width:615px;height:372px;background:var(--card)}
  .card--front{top:168px}
  .card--back{top:578px}

  .wordmark{position:absolute;font-family:"Mulish",sans-serif;font-weight:300;color:var(--purple);white-space:nowrap;letter-spacing:.5px}
  .card--front .wordmark{left:0;right:0;text-align:center;top:58px;font-size:50px}
  .card--back .wordmark{right:36px;top:52px;font-size:42px}

  .appointment{position:absolute;left:42px;right:43px;font-size:17.5px;display:flex;align-items:flex-end;gap:6px}
  .appointment .fill{flex:1;border-bottom:1px solid var(--rule);height:1px}
  .appointment--name{top:170px}
  .appointment--when{top:216px}
  .appointment .label + .fill + .label{margin-left:4px}

  .services-band{position:absolute;top:282px;left:0;width:494px;height:62px;background:var(--pink);color:#fff;font-size:17px;padding:8px 0 0 44px;line-height:25px}
  .services-band .sep{margin:0 13px}
  .band-end{position:absolute;top:282px;left:586px;width:29px;height:62px;background:var(--pink)}
  .partner{position:absolute;left:494px;top:278px;width:92px;height:70px;display:flex;flex-direction:column;align-items:center;justify-content:center;gap:4px;color:var(--partner);font-size:13px;font-weight:700;letter-spacing:1px}
  .partner .dot{width:30px;height:30px;border-radius:50%;background:var(--partner)}

  .person{position:absolute;left:38px;top:44px}
  .person h1{font-size:27px;font-weight:700;color:var(--purple);line-height:34px}
  .person p{font-size:15px;font-style:italic;line-height:19px}

  .contacts{position:absolute;left:46px;top:259px;list-style:none;font-size:16.5px}
  .contacts li{display:flex;align-items:center;height:25px}
  .contacts svg{width:15px;height:15px;margin-right:12px;fill:var(--pink)}

  .follow{position:absolute;right:36px;top:330px;font-size:16px;display:flex;gap:8px;align-items:baseline}
  .follow .network{color:var(--purple);font-size:13px}
  .bottom-band{position:absolute;left:0;bottom:0;width:100%;height:14px;background:var(--pink)}
</style>
</head>
<body>
  <section class="card card--front">
    <div class="wordmark">TL Glamworks</div>
    <div class="appointment appointment--name"><span class="label">Name:</span><span class="fill"></span></div>
    <div class="appointment appointment--when"><span class="label">Date:</span><span class="fill"></span><span class="label">Time:</span><span class="fill" style="flex:.55"></span></div>
    <div class="services-band">
      <div>Make-Up Tutorials<span class="sep">|</span>Bridal<span class="sep">|</span>Photography</div>
      <div>Debutante<span class="sep">|</span>Formals<span class="sep">|</span>Family Portraits</div>
    </div>
    <div class="partner"><span class="dot"></span><span>VELMORA</span></div>
    <div class="band-end"></div>
  </section>

  <section class="card card--back">
    <div class="person">
      <h1>Tessa Lowrie</h1>
      <p>Make-Up Artist</p>
      <p>Certificate III in Make-Up</p>
    </div>
    <div class="wordmark">TL Glamworks</div>
    <ul class="contacts">
      <li><svg viewBox="0 0 16 16" aria-hidden="true"><path d="M1 5c0-2 3-3 7-3s7 1 7 3v1h-4V5H5v1H1zM4 7h8l2 6H2z"/></svg>0462 318 725</li>
      <li><svg viewBox="0 0 16 16" aria-hidden="true"><path d="M1 3h14v10H1zm1.5 1.5v.3L8 9l5.5-4.2v-.3zm0 2.2v4.8l3-2.4zm11 0-3 2.4 3 2.4zM6.4 9.7l-3.6 2.8h10.4L9.6 9.7 8 11z"/></svg>tessalowrie@mailbox-demo.com</li>
      <li><svg viewBox="0 0 16 16" aria-hidden="true"><path d="M8 1a7 7 0 1 0 0 14A7 7 0 0 0 8 1zm-1 1.6V5H4.3A5.6 5.6 0 0 1 7 2.6zm2 0A5.6 5.6 0 0 1 11.7 5H9zM3.7 6.3H7v3H3.6a5.6 5.6 0 0 1 .1-3zm5.3 0h3.3a5.6 5.6 0 0 1 .1 3H9zM4.3 10.6H7v2.8a5.6 5.6 0 0 1-2.7-2.8zm4.7 0h2.7A5.6 5.6 0 0 1 9 13.4z"/></svg>tessalowrie.velmora-demo.com</li>
    </ul>
    <div class="follow">Follow on: <span class="network">Chatterbook</span><span class="network">Snapgram</span></div>
    <div class="bottom-band"></div>
  </section>
</body>
</html>
```